Industrial Company needing new business cards

We are a newly branded Industrial trade company. We specialise in Electrical, Mechanical and Air-conditioning.

I would like to see designs single sided. Focusing on the color scheme white/red/black and possibly gray. Possibly make it a black card with white writting... but open to all designs.

I would like the design to be professional, sleek and to the point.

Industry/Entity Type

Business

Contact Information for Business Card

Tom Harwell
Managing Director / Electrician
tomwork@vandilo.com.au
417 Calloway Street, Pembrook NSW 2458
Mobile: 0497551832
www.harwellindustrialgroup.com.au

Requirements
Must have
• Must be able to be sent in a manner that i can change the details for each employee.
• Our logo
Nice to have
• Would like it to somehow have " incorporating Barvo Group Pty Ltd" as this is the company we have taken over.
Should not have
• No yellow!!!
• must not simply place "barvo group" randomly on the business card. refer nice to have.

```html
<!DOCTYPE html>
<html lang="en">
<head>
<meta charset="utf-8">
<title>Harwell Industrial Group – Business Card</title>
<link href="https://fonts.googleapis.com/css2?family=Source+Sans+3:wght@400;600;700&display=swap" rel="stylesheet">
<style>
  :root {
    --page-bg: #3b3b3b;
    --card-white: #fbfbfb;
    --brand-red: #e0141e;
    --ink-black: #111111;
    --panel-black: #0b0b0b;
    --panel-glow: #2c2c2c;
    --text-white: #f2f2f2;
    --tag-grey: #6d6d6d;
  }
  * { box-sizing: border-box; margin: 0; padding: 0; }
  html, body {
    width: 1200px; height: 750px; overflow: hidden;
    background: var(--page-bg);
    font-family: "Source Sans 3", Arial, sans-serif;
  }
  .card {
    position: absolute; left: 75px; top: 74px;
    width: 1050px; height: 602px;
    background: var(--card-white);
    box-shadow: 0 6px 18px rgba(0,0,0,0.45);
    overflow: hidden;
  }
  .brand {
    position: absolute; left: 0; top: 0; width: 100%; height: 362px;
    display: flex; flex-direction: column; align-items: center; justify-content: center;
    gap: 14px;
  }
  .brand-name {
    display: flex; align-items: center; gap: 18px;
    font-weight: 700; font-size: 46px; letter-spacing: 1px;
    color: var(--ink-black); text-transform: uppercase;
  }
  .brand-mark {
    width: 30px; height: 30px; background: var(--brand-red);
  }
  .brand-services {
    font-weight: 600; font-size: 17px; letter-spacing: 1px;
    color: var(--tag-grey); text-transform: uppercase;
  }
  .divider {
    position: absolute; left: 0; top: 362px; width: 100%; height: 6px;
    background: var(--brand-red);
  }
  .panel {
    position: absolute; left: 0; top: 374px; width: 100%; height: 228px;
    background: radial-gradient(ellipse 45% 90% at 50% 10%, var(--panel-glow), var(--panel-black) 75%);
  }
  .divider-notch {
    position: absolute; left: 166px; top: 362px; width: 40px; height: 36px;
  }
  .person {
    position: absolute; left: 73px; top: 420px; color: var(--text-white);
  }
  .person-name {
    font-size: 37px; font-weight: 600; color: var(--brand-red); line-height: 1.1;
  }
  .person-role { font-size: 28px; line-height: 1.3; }
  .contacts {
    position: absolute; right: 60px; top: 424px;
    list-style: none; color: var(--text-white); font-size: 25px;
  }
  .contacts li {
    display: flex; align-items: center; justify-content: flex-end;
    gap: 18px; height: 40px;
  }
  .contacts svg { width: 26px; height: 28px; flex: none; }
</style>
</head>
<body>
  <main class="card">
    <header class="brand">
      <div class="brand-name"><span class="brand-mark"></span>Harwell Industrial Group</div>
      <div class="brand-services">Electrical - Mechanical - Airconditioning</div>
    </header>

    <div class="divider"></div>
    <section class="panel"></section>
    <svg class="divider-notch" viewBox="0 0 40 36" aria-hidden="true">
      <polygon points="0,0 40,0 20,30" fill="var(--brand-red)"/>
      <polygon points="6,6 34,6 20,22" fill="var(--card-white)"/>
      <polygon points="10,12 30,12 20,22" fill="var(--panel-black)"/>
    </svg>

    <section class="person">
      <h1 class="person-name">Tom Harwell</h1>
      <p class="person-role">Managing Director</p>
      <p class="person-role">Electrician</p>
    </section>

    <ul class="contacts">
      <li>0497551832
        <svg viewBox="0 0 26 28" aria-hidden="true">
          <rect x="6" y="1" width="14" height="26" rx="2.5" fill="none" stroke="var(--brand-red)" stroke-width="3"/>
          <rect x="9.5" y="21" width="7" height="2" fill="var(--brand-red)"/>
        </svg>
      </li>
      <li>tomwork@vandilo.com.au
        <svg viewBox="0 0 26 28" aria-hidden="true">
          <rect x="1" y="7" width="24" height="16" fill="var(--brand-red)"/>
          <polyline points="1,7 13,16 25,7" fill="none" stroke="var(--panel-black)" stroke-width="2"/>
        </svg>
      </li>
      <li>harwellindustrialgroup.com.au
        <svg viewBox="0 0 26 28" aria-hidden="true">
          <circle cx="13" cy="14" r="12" fill="var(--brand-red)"/>
          <ellipse cx="13" cy="14" rx="5" ry="12" fill="none" stroke="var(--panel-black)" stroke-width="1.8"/>
          <line x1="1" y1="14" x2="25" y2="14" stroke="var(--panel-black)" stroke-width="1.8"/>
        </svg>
      </li>
    </ul>
  </main>
</body>
</html>
```